Door Knockers/Cards

Tallbrook Exteriors - EST 1986
Specialist in custom exterior remodeling solutions for your home and cottage.
Book your free estimate today.
Tallbrook Exteriors Inc.
(555) 482-7316
sales@tallbrookexteriors-example.com
Founded in 1986 in Elmira, Ontario, Tallbrook Exteriors has grown to become an industry-leading provider of siding, eavestrough, railings, columns, windows, doors, and garage doors.
Our expert team provides custom remodeling services across Ontario for a wide variety of residential and commercial projects. From traditional exterior home remodels to luxurious custom homes, agricultural facilities, places of worship, retail buildings, and industrial businesses, Tallbrook Exteriors does it all.
**Would like to have a QR code if possible for clients to be linked to our site right away.**

```html
<!DOCTYPE html>
<html lang="en">
<head>
<meta charset="utf-8">
<title>Tallbrook Exteriors Door Hangers</title>
<link href="https://fonts.googleapis.com/css2?family=Bebas+Neue&family=Montserrat:ital,wght@0,400;0,500;0,700;0,800;1,700;1,800&display=swap" rel="stylesheet">
<style>
:root{
  --maroon:#62262a;
  --tan:#cdb3a4;
  --tan-light:#d6c0b2;
  --ink:#3b3b3b;
  --white:#ffffff;
  --bg:#b9babc;
  --black:#000000;
}
*{margin:0;padding:0;box-sizing:border-box}
html,body{width:1200px;height:2374px;overflow:hidden;background:var(--bg)}
body{position:relative;font-family:'Montserrat',sans-serif}
.hanger{position:absolute;top:607px;width:500px;height:1160px;background:var(--white);overflow:hidden}
.hanger--front{left:70px}
.hanger--back{left:630px}
.photo{position:absolute;left:0;top:0;width:500px;height:407px;border-radius:0 0 68px 68px}
.photo--house{background:linear-gradient(180deg,#e4e8ec 0%,#b9c6cf 30%,#9a9788 55%,#6f7f4e 78%,#a9a59d 100%)}
.photo--hall{background:linear-gradient(180deg,#eab59a 0%,#d9aa99 28%,#a9a39c 55%,#7d776f 78%,#5c5a58 100%)}
.die-cut{position:absolute;left:0;top:0;width:500px;height:230px}
.brand{position:absolute;left:0;top:452px;width:500px;display:flex;align-items:center;justify-content:center;gap:14px}
.brand__mark{width:30px;height:30px;background:var(--maroon)}
.brand__name{font-family:'Montserrat',sans-serif;font-weight:800;font-size:30px;color:var(--ink);letter-spacing:.5px}
.panel{position:absolute;left:0;top:573px;width:500px;height:587px;background:var(--maroon);border-radius:56px 56px 0 0}
.headline{position:absolute;left:0;width:500px;text-align:center;line-height:1}
.headline--one{top:633px;font-weight:800;font-size:50px;color:var(--white);letter-spacing:1px}
.headline--two{top:683px;font-weight:800;font-size:50px;color:var(--tan);letter-spacing:1px}
.headline--three{top:737px;font-family:'Bebas Neue',sans-serif;font-size:50px;color:var(--white)}
.intro{position:absolute;left:52px;top:790px;width:396px;font-size:14px;line-height:1.18;color:var(--white);text-align:justify;text-align-last:center}
.cta-pill{position:absolute;left:44px;top:886px;width:412px;height:59px;border-radius:30px;background:var(--tan);color:var(--white);font-family:'Bebas Neue',sans-serif;font-size:34px;display:flex;align-items:center;justify-content:center}
.call-label{position:absolute;left:0;width:500px;text-align:center;font-style:italic;font-weight:800;color:var(--white);font-size:25px}
.hanger--front .call-label{top:1001px}
.phone{position:absolute;left:0;width:500px;text-align:center;font-style:italic;font-weight:800;line-height:1}
.hanger--front .phone{top:1036px;font-size:52px;color:var(--tan)}
.address{position:absolute;left:0;top:1086px;width:500px;text-align:center;font-style:italic;font-weight:700;font-size:13.5px;color:var(--white)}
.web-pill{position:absolute;left:78px;top:1114px;width:344px;height:46px;background:var(--tan);border-radius:24px 24px 0 0;display:flex;align-items:center;justify-content:center;gap:6px;color:var(--white);font-style:italic;font-weight:700;font-size:13.5px}
.section-title{position:absolute;left:0;top:456px;width:500px;text-align:center;font-family:'Bebas Neue',sans-serif;font-size:40px;color:var(--maroon);line-height:1}
.service-list{position:absolute;left:40px;top:492px;width:420px;text-align:center;font-size:13.5px;line-height:1.2;color:var(--ink)}
.commercial{position:absolute;left:0;top:585px;width:500px;height:575px;background:var(--tan-light);border-radius:56px 56px 0 0}
.commercial-pill{position:absolute;left:43px;top:554px;width:414px;height:59px;border-radius:30px;background:var(--maroon);color:var(--white);font-family:'Bebas Neue',sans-serif;font-size:40px;display:flex;align-items:center;justify-content:center}
.service{position:absolute;left:50px;width:410px;height:80px}
.service__title{font-family:'Bebas Neue',sans-serif;font-size:25px;color:var(--maroon);line-height:1}
.service__text{width:305px;margin-top:4px;font-size:10.5px;line-height:1.22;color:var(--ink)}
.service__photo{position:absolute;right:0;top:0;width:74px;height:74px;border-radius:50%;border:2px solid var(--maroon)}
.service__photo--a{background:linear-gradient(160deg,#c7c3bd,#7b4a33 60%,#4f5a3a)}
.service__photo--b{background:linear-gradient(160deg,#dfe6ee,#b6bcc3 55%,#7b7d80)}
.service__photo--c{background:linear-gradient(160deg,#e9e2c9,#b9b7ad 55%,#8d8f92)}
.service__photo--d{background:linear-gradient(160deg,#f0ede8,#c9c4bd 55%,#4d4a47)}
.footer-band{position:absolute;left:0;top:1015px;width:500px;height:145px;background:var(--maroon);border-radius:56px 56px 0 0}
.hanger--back .call-label{top:1040px}
.hanger--back .phone{top:1078px;font-size:50px;color:var(--white)}
</style>
</head>
<body>

<section class="hanger hanger--front">
  <div class="photo photo--house" role="img" aria-label="Photo of a large stone two-storey home with landscaped lawn and driveway under a partly cloudy sky"></div>
  <svg class="die-cut" viewBox="0 0 500 230" aria-hidden="true">
    <line x1="100" y1="0" x2="254" y2="153" stroke="#000" stroke-width="7"/>
    <circle cx="254" cy="153" r="68" fill="#000"/>
  </svg>
  <div class="brand">
    <span class="brand__mark"></span>
    <span class="brand__name">Tallbrook Exteriors Inc.</span>
  </div>
  <div class="panel"></div>
  <h1 class="headline headline--one">EXTERIOR</h1>
  <p class="headline headline--two">REMODELLING</p>
  <p class="headline headline--three">SOLUTIONS YOUR HOME</p>
  <p class="intro">Providing expert residential siding, eavestrough, railings, columns, windows, doors, and garage door installation across Southwestern Ontario, from Kitchener-Waterloo to London and Oakville to Muskoka.</p>
  <div class="cta-pill">BOOK YOUR FREE ESTIMATE TODAY.</div>
  <p class="call-label">CALL NOW TODAY!</p>
  <p class="phone">555-482-7316</p>
  <p class="address">120 Cedar Lane North Elmvale, ON A1B 2C3</p>
  <div class="web-pill">
    <svg width="16" height="16" viewBox="0 0 16 16" aria-hidden="true"><g fill="none" stroke="#fff" stroke-width="1.2"><circle cx="8" cy="8" r="6.5"/><ellipse cx="8" cy="8" rx="3" ry="6.5"/><line x1="1.5" y1="8" x2="14.5" y2="8"/></g></svg>
    <span>www.tallbrookexteriors-example.com</span>
  </div>
</section>

<section class="hanger hanger--back">
  <div class="photo photo--hall" role="img" aria-label="Photo of a metal-roofed fire hall with open bay doors and trucks at dusk under a peach sky"></div>
  <svg class="die-cut" viewBox="0 0 500 230" aria-hidden="true">
    <line x1="400" y1="0" x2="246" y2="153" stroke="#000" stroke-width="7"/>
    <circle cx="246" cy="153" r="68" fill="#000"/>
  </svg>
  <h2 class="section-title">RESIDENTIAL SERVICES</h2>
  <p class="service-list">Siding | Eavestrough | Mouldings and Trims | Columns and Railings | Doors | Windows | Garage Doors</p>
  <div class="commercial"></div>
  <div class="commercial-pill">COMMERCIAL SERVICES</div>

  <div class="service" style="top:650px">
    <h3 class="service__title">SIDING</h3>
    <p class="service__text">Our network of industry-leading manufacturers ensure that we can provide any type of siding imaginable to help you get the look you want for a price that works.</p>
    <div class="service__photo service__photo--a" role="img" aria-label="Photo of a building with new siding"></div>
  </div>
  <div class="service" style="top:745px">
    <h3 class="service__title">SOFFIT, FASCIA, &amp; EAVESTROUGH</h3>
    <p class="service__text">Add practicality and beauty to the exterior of your business with professionally installed soffit, fascia, and eavestrough.</p>
    <div class="service__photo service__photo--b" role="img" aria-label="Photo of a building roofline with soffit and eavestrough"></div>
  </div>
  <div class="service" style="top:840px">
    <h3 class="service__title">WINDOWS &amp; DOORS</h3>
    <p class="service__text">Transform the way people are welcomed into your business. Increase natural light and improve safety and energy-efficiency with new windows and doors.</p>
    <div class="service__photo service__photo--c" role="img" aria-label="Photo of a storefront with windows and doors"></div>
  </div>
  <div class="service" style="top:935px">
    <h3 class="service__title">ARCHITECTURAL MOULDING AND TRIM</h3>
    <p class="service__text">From ornate to contemporary, add style to your commercial building that will instantly help your business stand out.</p>
    <div class="service__photo service__photo--d" role="img" aria-label="Photo of a commercial entrance with architectural trim"></div>
  </div>

  <div class="footer-band"></div>
  <p class="call-label">CALL NOW TODAY!</p>
  <p class="phone">555-482-7316</p>
</section>

</body>
</html>
```